equestrian poster

Could you make the poster an elete looking poster for a sports event using the building on the back ground and photo shop the horse there also please make an sporty luxery poster
the dates for next year are 27th till 31 st may and 16 till 19 plus 23rd till 26 juli

our colors are green and gray

Target Market(s)

tourist and public

Industry/Entity Type

equestrian event interna

Other font styles liked:
• caslon classico font

Colors
00AB8E
00BBA5
67D7C9
C6EFE9
E9F9F6

```html
<!DOCTYPE html>
<html lang="en">
<head>
<meta charset="utf-8">
<title>CH Ravenhorst – Show Jumping 2026</title>
<link rel="stylesheet" href="https://fonts.googleapis.com/css2?family=Libre+Caslon+Text:ital,wght@0,400;0,700;1,400;1,700&display=swap">
<style>
  :root{
    --green:#00AB8E;
    --green-2:#00BBA5;
    --green-3:#67D7C9;
    --green-4:#C6EFE9;
    --green-5:#E9F9F6;
    --ink:#1f3b33;
    --gray:#9a9c9e;
    --gray-light:#c9cacb;
    --backdrop:#363d40;
    --paper:#ffffff;
  }
  *{margin:0;padding:0;box-sizing:border-box}
  html,body{width:1200px;height:1200px;overflow:hidden}
  body{background:var(--backdrop);font-family:"Libre Caslon Text",Georgia,serif;position:relative}
  .poster{position:absolute;left:217px;top:76px;width:742px;height:1050px;background:var(--paper);overflow:hidden;box-shadow:0 4px 14px rgba(0,0,0,.35)}
  .title{position:absolute;top:52px;width:100%;text-align:center;color:var(--green);font-weight:700;font-size:50px;letter-spacing:3px;line-height:1}
  .since{position:absolute;top:116px;width:100%;text-align:center;color:var(--green);font-weight:700;font-size:22px;letter-spacing:5px;line-height:1}
  .hero{position:absolute;left:70px;top:148px;width:610px;height:580px}
  .hero svg{display:block}
  .logos{position:absolute;top:752px;left:0;width:100%;display:flex;justify-content:center;gap:56px;align-items:center}
  .logo{display:flex;flex-direction:column;align-items:center;gap:6px;color:var(--ink);font-size:15px}
  .logo-dot{width:64px;height:64px;border-radius:50%;background:var(--green-4)}
  .dates{position:absolute;top:882px;left:46px;width:675px;display:flex}
  .date{flex:1;text-align:center;position:relative}
  .date + .date::before{content:"";position:absolute;left:0;top:0;width:1px;height:92px;background:var(--gray-light);transform:skewX(-12deg)}
  .days{color:var(--green);font-weight:700;font-size:25px;line-height:1}
  .days sup{font-size:14px;vertical-align:9px}
  .month{color:var(--green);font-weight:700;font-size:28px;line-height:1.2}
  .classes{margin:8px auto 0;width:186px;height:23px;background:linear-gradient(90deg,var(--gray),var(--gray-light));transform:skewX(-18deg);display:flex;align-items:center;justify-content:center}
  .classes span{transform:skewX(18deg);font-style:italic;font-size:12px;color:#2c2e30}
  .footer-shadow{position:absolute;left:0;top:994px;width:742px;height:31px;background:linear-gradient(90deg,#b7b8b9,#e5e5e5)}
  .footer{position:absolute;left:34px;top:986px;width:678px;height:31px;background:var(--green);transform:skewX(-18deg);display:flex;align-items:center;justify-content:center;gap:40px}
  .footer-item{transform:skewX(18deg);display:flex;align-items:center;gap:7px;color:#fff;font-size:12px}
  .icon-dot{width:15px;height:15px;border-radius:50%;background:#fff}
</style>
</head>
<body>
  <main class="poster">
    <h1 class="title">CH RAVENHORST</h1>
    <p class="since">SINCE 2005</p>

    <div class="hero">
      <svg width="610" height="580" viewBox="0 0 610 580">
        <defs>
          <linearGradient id="photoTone" x1="0" y1="0" x2="1" y2="0">
            <stop offset="0" stop-color="#8a5a3a"/>
            <stop offset="0.3" stop-color="#6f7a5c"/>
            <stop offset="0.5" stop-color="#4f8f78"/>
            <stop offset="0.7" stop-color="#b9bcbd"/>
            <stop offset="1" stop-color="#dcdedf"/>
          </linearGradient>
          <linearGradient id="fadeDown" x1="0" y1="0" x2="0" y2="1">
            <stop offset="0.75" stop-color="#fff" stop-opacity="0"/>
            <stop offset="1" stop-color="#fff" stop-opacity="0.9"/>
          </linearGradient>
        </defs>
        <polygon points="120,20 160,20 20,420 -20,420" fill="var(--green-4)"/>
        <polygon points="520,60 570,60 400,560 350,560" fill="var(--green-3)" opacity=".7"/>
        <polygon points="585,140 610,140 470,560 445,560" fill="var(--green-4)"/>
        <g role="img" aria-label="Two show jumpers clearing fences, a bay horse and a grey horse, in front of the wooden-gabled clubhouse with green-lit windows">
          <rect x="40" y="10" width="530" height="540" rx="18" fill="url(#photoTone)"/>
          <rect x="40" y="10" width="530" height="540" rx="18" fill="url(#fadeDown)"/>
        </g>
      </svg>
    </div>

    <div class="logos">
      <div class="logo"><span class="logo-dot"></span><span>Meadow Tour</span></div>
      <div class="logo"><span class="logo-dot"></span><span>C.H. Ravenhorst</span></div>
    </div>

    <section class="dates">
      <div class="date">
        <div class="days">27<sup>TH</sup> - 31<sup>ST</sup></div>
        <div class="month">MAY 2026</div>
        <div class="classes"><span>CSI 2* / CSI 1* / CSI 1* YH</span></div>
      </div>
      <div class="date">
        <div class="days">16<sup>TH</sup> - 19<sup>TH</sup></div>
        <div class="month">JULI 2026</div>
        <div class="classes"><span>CSI 2* / CSI 1* / CSI 1* YH</span></div>
      </div>
      <div class="date">
        <div class="days">23<sup>RD</sup> - 26<sup>TH</sup></div>
        <div class="month">JULI 2026</div>
        <div class="classes"><span>CSI 2* / CSI 1* / CSI 1* YH</span></div>
      </div>
    </section>

    <div class="footer-shadow"></div>
    <div class="footer">
      <div class="footer-item"><span class="icon-dot"></span><span>CH Ravenhorst - CSI** LINDENVELD</span></div>
      <div class="footer-item">
        <svg width="15" height="15" viewBox="0 0 18 18" fill="none" stroke="#fff" stroke-width="1.4">
          <circle cx="9" cy="9" r="7.5"/><ellipse cx="9" cy="9" rx="3.3" ry="7.5"/><line x1="1.5" y1="9" x2="16.5" y2="9"/>
        </svg>
        <span>www.chravenhorst.nl</span>
      </div>
    </div>
  </main>
</body>
</html>
```